Quillstone Restaurnt Lunch Menu Redesign:

We have two lunch special menus that need to be reformatted into a 4.25inx11in and need a graphics design update. Some menu items need to change and some descriptions need to updated. This new menu should double sided with the Main Dining Lunch Menu on the front side and Teppanyaki Lunch menu on the back.

Both menus should follow the same design formatting as the main dining lunch menu (font, sizing, ect.)

```html
<!DOCTYPE html>
<html lang="en">
<head>
<meta charset="utf-8">
<title>Quillstone Restaurant – Lunch Specials</title>
<link rel="stylesheet" href="https://fonts.googleapis.com/css2?family=Kaushan+Script&family=Montserrat:wght@500;600&family=Open+Sans:ital,wght@0,400;0,600;1,400&family=Playfair+Display:wght@900&display=swap">
<style>
  :root{
    --navy:#0b2a8c;
    --ink:#1f1f24;
    --price:#5a5a62;
    --muted:#3c3c44;
    --row:#f1f1f4;
    --row-strong:#e9e9ec;
    --gold:#b89a5e;
    --page:#ffffff;
    --stage:#f3f3f5;
  }
  *{box-sizing:border-box;margin:0;padding:0}
  html,body{width:932px;height:1200px;overflow:hidden;background:var(--stage)}
  body{position:relative;font-family:"Open Sans",Arial,sans-serif;color:var(--ink)}
  .menu{position:absolute;top:83px;width:399px;height:1034px;background:var(--page);overflow:hidden;
        box-shadow:0 6px 24px rgba(20,20,40,.08)}
  .menu--dining{left:44px}
  .menu--teppanyaki{left:489px}
  .brand{position:absolute;top:20px;left:0;width:100%;text-align:center;font-family:"Open Sans",Arial,sans-serif;
         font-weight:600;font-size:15px;color:var(--navy);letter-spacing:.5px}
  .brand::after{content:"";display:inline-block;width:6px;height:6px;border-radius:50%;background:var(--navy);margin-left:5px;vertical-align:middle}
  .title{position:absolute;top:54px;left:0;width:100%;text-align:center;font-family:"Playfair Display",Georgia,serif;
         font-weight:900;font-size:28px;color:var(--navy);letter-spacing:-.3px}
  .hours{position:absolute;top:96px;left:0;width:100%;display:flex;justify-content:center;align-items:center;gap:6px;
         font-family:"Montserrat",Arial,sans-serif;font-weight:600;font-size:8.5px;color:var(--navy)}
  .hours::before,.hours::after{content:"";width:26px;height:1px;background:var(--ink)}
  .banner{position:absolute;left:40px;width:160px;height:32px}
  .banner svg{position:absolute;inset:0}
  .banner span{position:relative;display:block;text-align:center;line-height:34px;font-family:"Kaushan Script",cursive;
               font-size:19px;color:#fff;white-space:nowrap;letter-spacing:-.3px}
  .note{position:absolute;left:39px;font-size:7.1px;line-height:8.4px;color:var(--muted);padding:0 8px 3px 0;
        border-bottom:1px solid #e2e2e6;white-space:nowrap}
  .photo{position:absolute;left:249px;width:113px;height:58px;border-radius:50%}
  .row{position:absolute;left:38px;width:323px;display:flex;align-items:center;justify-content:space-between;
       padding:0 8px 0 2px}
  .row.shade{background:var(--row)}
  .row.shade-strong{background:var(--row-strong)}
  .name{font-size:12px;line-height:13px}
  .desc{font-style:italic;font-size:9px;line-height:11px}
  .inline-desc{font-style:italic;font-size:9px}
  .price{font-size:11.5px;color:var(--price);white-space:nowrap}
  .sushi{position:absolute;height:22px;display:flex;align-items:center;padding-left:2px;font-size:12px}
  .sushi em{font-size:9px;margin-left:4px}
  .sushi.left{left:38px;width:139px}
  .sushi.right{left:223px;width:138px}
  .sushi.indent{left:229px;width:132px}
  .sushi.shade{background:var(--row)}
  .divider{position:absolute;left:224px;top:505px;width:1.5px;height:90px;background:var(--gold)}
  .footer{position:absolute;top:997px;left:0;width:100%;text-align:center;font-size:8px;line-height:10px;font-style:italic}
  .footer b{font-style:normal}
  .plates{position:absolute;left:0;top:830px}
</style>
</head>
<body>

<section class="menu menu--dining">
  <div class="brand">Quillstone</div>
  <h1 class="title">Lunch Specials</h1>
  <div class="hours">Served Daily 11AM - 3PM</div>

  <div class="banner" style="top:133px">
    <svg viewBox="0 0 160 32" preserveAspectRatio="none"><path d="M0 4 Q80 -3 160 4 L160 32 L0 32 Z" fill="var(--navy)"/></svg>
    <span>Sandwiches</span>
  </div>
  <div class="photo" role="img" aria-label="Photo of a burger with fries" style="top:124px;background:radial-gradient(ellipse at 50% 45%,#7a4a2a,#3a2418 60%,#5c5c5c)"></div>
  <p class="note" style="top:171px">Served with Choice of Miso Soup or House Salad &amp; Potato Chips</p>

  <div class="row" style="top:185px;height:37px"><div><div class="name">Fried Breaded Calamari Steak</div><div class="desc">with Tomato, Lettuce &amp; Onion</div></div><span class="price">$ 16</span></div>
  <div class="row shade" style="top:222px;height:37px"><div><div class="name">Grilled Chicken <span class="inline-desc">with Bacon, Tomato,</span></div><div class="desc">Lettuce &amp; Mayonnaise Drizzle</div></div><span class="price">$ 16</span></div>
  <div class="row" style="top:259px;height:40px"><div><div class="name">Hamburger <span class="inline-desc">with Lettuce, Tomato,</span></div><div class="desc">Onion, Mayonnaise Drizzle</div></div><span class="price">$ 18</span></div>
  <div class="row shade" style="top:299px;height:34px"><div><div class="name">Fried Soft Shell Crab Burger</div><div class="desc">with Avocado, Lettuce, Tomato, Onion &amp; Mayo</div></div><span class="price">$ 20</span></div>

  <div class="banner" style="top:365px">
    <svg viewBox="0 0 160 32" preserveAspectRatio="none"><path d="M0 4 Q80 -3 160 4 L160 32 L0 32 Z" fill="var(--navy)"/></svg>
    <span>Sushi Specials</span>
  </div>
  <div class="photo" role="img" aria-label="Photo of a sushi roll on a dark plate" style="top:360px;background:radial-gradient(ellipse at 50% 50%,#e08a5a,#6a8a3a 45%,#2a2a2a)"></div>
  <p class="note" style="top:404px;border:none">Please Select 4 of the followings for $16<br>Served with a 4 piece California Roll &amp; Miso Soup or House Salad</p>

  <div class="sushi left" style="top:430px">Hamachi<em>Yellowtail Tuna</em></div>
  <div class="sushi left shade" style="top:456px">Hotate<em>Yellowtail</em></div>
  <div class="sushi left" style="top:482px">Ika<em>Squid</em></div>
  <div class="sushi left shade" style="top:508px">Ikura<em>Salmon Roe</em></div>
  <div class="sushi left" style="top:534px">Saba<em>Mackerel</em></div>
  <div class="sushi left shade" style="top:559px">Sake<em>Salmon</em></div>
  <div class="sushi left" style="top:585px">Tai<em>Red Snapper</em></div>
  <div class="sushi right" style="top:430px">Maguro<em>Yellowtail Tuna</em></div>
  <div class="sushi right shade" style="top:456px">Smoked Salmon</div>
  <div class="divider"></div>
  <div class="sushi indent" style="top:500px">Tako<em>Octopus</em></div>
  <div class="sushi indent" style="top:525px">Unagi<em>BBQ Eel</em></div>
  <div class="sushi indent" style="top:551px">Ebi<em>Shrimp</em></div>
  <div class="sushi indent" style="top:577px">Tamago<em>Egg</em></div>

  <div class="banner" style="top:634px">
    <svg viewBox="0 0 160 32" preserveAspectRatio="none"><path d="M0 4 Q80 -3 160 4 L160 32 L0 32 Z" fill="var(--navy)"/></svg>
    <span>Main Courses</span>
  </div>
  <div class="photo" role="img" aria-label="Photo of teriyaki with grilled vegetables" style="top:627px;background:radial-gradient(ellipse at 45% 55%,#6a3a1e,#3a2012 55%,#c9a23a)"></div>
  <p class="note" style="top:673px">Served with Rice &amp; Choice of Miso Soup or House Salad<br>All Meals Served with Rice. Upgrade to fried rice for only $4</p>

  <div class="row" style="top:698px;height:38px"><div><div class="name">Organic Tofu Teriyaki</div><div class="desc">Served Grilled or Tempura Fried</div></div><span class="price">$ 14</span></div>
  <div class="row shade" style="top:736px;height:21px"><span class="name">Chicken Teriyaki</span><span class="price">$ 16</span></div>
  <div class="row" style="top:760px;height:22px"><span class="name">Spicy Chicken Teriyaki</span><span class="price">$ 16</span></div>
  <div class="row shade" style="top:786px;height:22px"><span class="name">Beef Teriyaki</span><span class="price">$ 16</span></div>
  <div class="row" style="top:812px;height:22px"><span class="name">Spicy Beef Teriyaki</span><span class="price">$ 16</span></div>
  <div class="row shade" style="top:838px;height:33px"><div><div class="name">Chicken Kats</div><div class="desc">Breaded Chicken Breast</div></div><span class="price">$ 15</span></div>
  <div class="row" style="top:874px;height:34px"><div><div class="name">Katsu Don</div><div class="desc">Fried Chicken Breast, Egg &amp; Onion over Rice</div></div><span class="price">$ 16</span></div>
  <div class="row shade" style="top:912px;height:33px"><div><div class="name">Unagi Don</div><div class="desc">BBQ Eel over Rice</div></div><span class="price">$ 19</span></div>
  <div class="row" style="top:949px;height:22px"><span class="name">Shrimp &amp; Vegetable Tempura</span><span class="price">$ 16</span></div>

  <p class="footer"><b>Served Raw:</b> 20% gratuity added to parties of 6 or more.<br>Consuming raw or undercooked food may increase your risk of foodborne illness</p>
</section>

<section class="menu menu--teppanyaki">
  <div class="brand">Quillstone</div>
  <h1 class="title">Lunch Specials</h1>
  <div class="hours">Served Daily 11AM - 3PM</div>

  <div class="banner" style="top:133px">
    <svg viewBox="0 0 160 32" preserveAspectRatio="none"><path d="M0 4 Q80 -3 160 4 L160 32 L0 32 Z" fill="var(--navy)"/></svg>
    <span>Teppanyaki Lunch</span>
  </div>
  <div class="photo" role="img" aria-label="Photo of hibachi chicken with fried rice" style="top:124px;background:radial-gradient(ellipse at 50% 50%,#8a5a2e,#4a2e18 55%,#6a6a6a)"></div>
  <p class="note" style="top:171px">Served with Miso Soup or Salad, Choice of Rice &amp; Vegetables</p>

  <div class="row" style="top:188px;height:22px"><span class="name">Hibachi Chicken</span><span class="price">$ 18</span></div>
  <div class="row shade" style="top:214px;height:22px"><span class="name">Hibachi Shrimp</span><span class="price">$ 19</span></div>
  <div class="row" style="top:240px;height:22px"><span class="name">Hibachi New York Steak</span><span class="price">$ 20</span></div>
  <div class="row shade" style="top:266px;height:22px"><span class="name">Hibachi Salmon</span><span class="price">$ 20</span></div>
  <div class="row" style="top:292px;height:22px"><span class="name">Teriyaki Beef</span><span class="price">$ 19</span></div>
  <div class="row shade" style="top:318px;height:22px"><span class="name">Hibachi Scallop</span><span class="price">$ 20</span></div>
  <div class="row" style="top:344px;height:22px"><span class="name">Chicken and Shrimp</span><span class="price">$ 21</span></div>
  <div class="row shade" style="top:370px;height:22px"><span class="name">Scallop and Shrimp</span><span class="price">$ 22</span></div>
  <div class="row" style="top:396px;height:22px"><span class="name">New York Steak and Chicken</span><span class="price">$ 22</span></div>
  <div class="row shade" style="top:422px;height:22px"><span class="name">New York Steak and Shrimp</span><span class="price">$ 23</span></div>
  <div class="row" style="top:448px;height:22px"><span class="name">New York Steak and Scallop</span><span class="price">$ 24</span></div>
  <div class="row shade" style="top:474px;height:22px"><span class="name">Filet Mignon</span><span class="price">$ 23</span></div>
  <div class="row" style="top:500px;height:22px"><span class="name">Filet Mignon and Chicken</span><span class="price">$ 25</span></div>
  <div class="row shade" style="top:526px;height:22px"><span class="name">Filet Mignon and Shrimp</span><span class="price">$ 26</span></div>
  <div class="row" style="top:552px;height:22px"><span class="name">Filet Mignon and Scallop</span><span class="price">$ 27</span></div>

  <div class="banner" style="top:608px">
    <svg viewBox="0 0 160 32" preserveAspectRatio="none"><path d="M0 4 Q80 -3 160 4 L160 32 L0 32 Z" fill="var(--navy)"/></svg>
    <span>Special Menu</span>
  </div>
  <div class="photo" role="img" aria-label="Photo of teriyaki beef with fried rice" style="top:604px;height:52px;background:radial-gradient(ellipse at 40% 50%,#5a3420,#3a2214 45%,#d8b46a)"></div>
  <p class="note" style="top:646px">Ages 12 and Under ~ Ages 65 and Older<br>Served with Miso Soup or Salad, Choice of Rice &amp; Vegetables</p>

  <div class="row" style="top:677px;height:22px"><span class="name">Hibachi Chicken</span><span class="price">$ 15</span></div>
  <div class="row shade-strong" style="top:703px;height:22px"><span class="name">Hibachi Shrimp</span><span class="price">$ 16</span></div>
  <div class="row" style="top:729px;height:22px"><span class="name">Hibachi New York Steak</span><span class="price">$ 18</span></div>
  <div class="row shade-strong" style="top:755px;height:22px"><span class="name">Hibachi Scallop</span><span class="price">$ 18</span></div>
  <div class="row" style="top:781px;height:22px"><span class="name">Teriyaki Beef</span><span class="price">$ 16</span></div>

  <svg class="plates" width="399" height="204" viewBox="0 830 399 204">
    <defs>
      <radialGradient id="tempuraTone" cx="50%" cy="55%" r="60%">
        <stop offset="0" stop-color="#e6b44a"/><stop offset=".7" stop-color="#c98a2a"/><stop offset="1" stop-color="#5a6a9a"/>
      </radialGradient>
      <radialGradient id="sandwichTone" cx="45%" cy="40%" r="60%">
        <stop offset="0" stop-color="#e8dcc4"/><stop offset=".55" stop-color="#8a6a4a"/><stop offset="1" stop-color="#3a5a2a"/>
      </radialGradient>
    </defs>
    <circle cx="82" cy="949" r="86" fill="none" stroke="var(--navy)" stroke-width="1.2"/>
    <circle cx="78" cy="951" r="80" fill="url(#tempuraTone)" role="img" aria-label="Photo of shrimp and vegetable tempura with rice"/>
    <circle cx="273" cy="1022" r="114" fill="none" stroke="var(--navy)" stroke-width="1.2"/>
    <circle cx="271" cy="1026" r="108" fill="url(#sandwichTone)" role="img" aria-label="Photo of a toasted sandwich with salad"/>
  </svg>
</section>

</body>
</html>
```